Corvane USA PowerPoint Template

I need a generic PPT template for my business, need to incorporate my logo and colors, need a professional look, master slide should have a title bar at top with logo right, a light logo watermark on the body section, and a page number at the bottom of each page. I've attached the first presentation for this template, but I'll use this template for all company presentations.

Target Market(s)

Investors, clients.

Font styles to use
Sans Serif
Other font styles liked:
• You choose. Professional and modern.

```html
<!DOCTYPE html>
<html lang="en">
<head>
<meta charset="utf-8">
<title>Corvane USA Presentation Template</title>
<link href="https://fonts.googleapis.com/css2?family=Poppins:wght@400;500;600;700;800&display=swap" rel="stylesheet">
<style>
:root{
  --navy:#14295a;
  --navy-deep:#0c1a3d;
  --blue:#2b5486;
  --red:#b5001d;
  --ink:#2b2f3a;
  --muted:#5b6170;
  --paper:#f3f4f7;
  --line:#d9dce3;
  --stage:#a9a9a9;
}
*{margin:0;padding:0;box-sizing:border-box}
html,body{width:1012px;height:1200px;overflow:hidden;background:var(--stage)}
body{position:relative;font-family:'Poppins',sans-serif;color:var(--ink)}
.slide{position:absolute;width:801px;height:450px;overflow:hidden;transform:scale(.5737);transform-origin:0 0;
  background:linear-gradient(135deg,#fafbfc 0%,var(--paper) 55%,#eceef2 100%)}
.s-cover{left:31.6px;top:37.9px}
.s-adv{left:521px;top:37.9px}
.s-toc{left:31.6px;top:326.4px}
.s-plan{left:521px;top:326.4px}
.s-situ{left:31.6px;top:615.6px}
.s-blank{left:521px;top:615.6px}
.s-market{left:31.6px;top:904.1px}
.s-thanks{left:521px;top:904.1px}
.abs{position:absolute}
.title{position:absolute;left:44px;top:26px;font-size:24px;line-height:1.3;font-weight:700;color:var(--navy);letter-spacing:.2px}
.title em{font-style:normal;color:var(--red)}
.brand{position:absolute;right:46px;top:36px;display:flex;align-items:center;gap:6px}
.brand .mark{width:16px;height:16px;background:var(--red)}
.brand .name{font-size:15px;font-weight:800;color:var(--navy);white-space:nowrap}
.footer{position:absolute;left:0;right:0;top:408px;border-top:1px solid var(--line)}
.copyright{position:absolute;left:44px;top:420px;font-size:9.5px;font-weight:500;color:#222}
.pagenum{position:absolute;left:736px;top:419px;width:19px;height:19px;background:var(--navy);color:#fff;font-size:9px;font-weight:500;display:flex;align-items:center;justify-content:center}
/* cover */
.s-cover{background:linear-gradient(120deg,var(--navy-deep) 0%,#1b3668 70%)}
.cover-brand{position:absolute;left:66px;top:72px;display:flex;align-items:center;gap:10px}
.cover-brand .mark{width:26px;height:26px;background:#fff}
.cover-brand .name{font-size:30px;font-weight:800;color:#fff}
.welcome{position:absolute;left:66px;top:292px;color:#fff;font-size:15px;font-weight:400}
.cover-name{position:absolute;left:66px;top:310px;color:#fff;font-size:38px;font-weight:700}
.cover-lede{position:absolute;left:68px;top:362px;width:300px;color:#dfe5f1;font-size:8px;line-height:1.5}
/* advantages */
.adv-card{position:absolute;width:355px;height:57px;background:#fff;box-shadow:0 1px 4px rgba(20,41,90,.08);padding:11px 12px 0 46px}
.adv-card .num{position:absolute;left:12px;top:12px;font-size:19px;font-weight:700;color:var(--red)}
.adv-card h3{font-size:9.5px;font-weight:700;color:var(--navy);line-height:1.25;text-transform:uppercase}
.adv-card p{font-size:7.8px;color:var(--muted);margin-top:5px}
/* toc */
.toc-num{position:absolute;width:67px;height:66px;background:linear-gradient(135deg,#d2001f,#8c0016);color:#fff;font-size:22px;font-weight:700;display:flex;align-items:center;justify-content:center}
.toc-num::before{content:"";position:absolute;left:0;top:25px;border-left:9px solid #fff;border-top:8px solid transparent;border-bottom:8px solid transparent}
.toc-body{position:absolute;width:266px;height:66px;background:linear-gradient(90deg,var(--navy-deep),var(--blue));color:#fff;padding:10px 18px}
.toc-body h3{font-size:10px;font-weight:600}
.toc-body p{font-size:7.8px;line-height:1.5;margin-top:6px;color:#dbe3f0}
/* plan */
.plan-img{position:absolute;top:112px;width:165px;height:151px}
.plan-col{position:absolute;top:270px;width:165px;text-align:center}
.plan-col h3{font-size:10.5px;font-weight:600;color:var(--navy);line-height:1.5}
.plan-col p{font-size:7.6px;line-height:2.1;color:#333;margin-top:6px}
/* situation */
.situ-photo{position:absolute;left:0;top:0;width:254px;height:450px;background:linear-gradient(160deg,#3d5f9e 0%,#6d8cc6 45%,#1d3366 100%)}
.situ-title{left:276px;top:104px}
.situ-col{position:absolute;top:150px;font-size:8.2px;line-height:1.6;color:#333}
.situ-col .item{position:relative;padding-left:20px;margin-bottom:9px}
.situ-col .item::before{content:"";position:absolute;left:2px;top:3px;width:8px;height:8px;
  background:radial-gradient(circle,var(--red) 45%,transparent 50%) 0 0/3px 3px}
.situ-col ul{list-style:none;margin:8px 0 0 16px}
.situ-col li{position:relative;padding-left:12px}
.situ-col li::before{content:"»";position:absolute;left:0;color:var(--red)}
.situ-col .phase{font-weight:600;margin:6px 0 4px 16px}
.situ-col .phase-list{margin:0 0 8px 16px}
/* market */
.market-lede{position:absolute;left:45px;top:58px;width:530px;font-size:11px;line-height:1.55;color:#444}
.icon-box{position:absolute;width:45px;height:45px;border:1.5px solid var(--navy);display:flex;align-items:center;justify-content:center}
.mk-col{position:absolute;top:138px;width:270px}
.mk-col h2{font-size:13px;font-weight:600;color:var(--navy);margin-bottom:10px}
.mk-col h4{font-size:9.5px;font-weight:600;color:#111;margin-top:12px}
.mk-col p{font-size:7.8px;line-height:1.6;color:#555;margin-top:5px}
/* watermark */
.watermark{position:absolute;left:220px;top:115px;width:360px;height:200px;display:flex;align-items:center;justify-content:center;gap:10px;opacity:.12}
.watermark .mark{width:40px;height:40px;border:4px solid var(--navy)}
.watermark .name{font-size:30px;font-weight:800;color:var(--navy);white-space:nowrap}
/* thanks */
.s-thanks{background:linear-gradient(120deg,var(--navy-deep) 0%,#27508a 100%)}
.thanks-brand{position:absolute;left:0;right:0;top:60px;display:flex;align-items:center;justify-content:center;gap:10px}
.thanks-brand .mark{width:26px;height:26px;background:#fff}
.thanks-brand .name{font-size:32px;font-weight:800;color:#fff}
.thanks-word{position:absolute;left:0;right:0;top:342px;text-align:center;font-size:40px;line-height:1;font-weight:800;color:var(--navy)}
.thanks-word em{font-style:normal;color:var(--red)}
.thanks-lede{position:absolute;left:230px;width:340px;top:390px;text-align:center;font-size:8px;line-height:1.5;color:#444}
</style>
</head>
<body>

<!-- Cover -->
<section class="slide s-cover">
  <svg class="abs" width="801" height="450" viewBox="0 0 801 450">
    <path role="img" aria-label="Photo of two engineers reviewing a tablet in a cable factory" d="M610,0 L801,0 L801,450 L660,450 C520,380 470,250 500,150 C520,80 560,30 610,0 Z" fill="#9aa3ad"/>
    <path d="M555,0 L610,0 C560,30 520,80 500,150 C470,250 520,380 660,450 L605,450 C465,380 430,250 462,150 C485,80 515,30 555,0 Z" fill="var(--red)"/>
    <path d="M597,0 L610,0 C560,30 520,80 500,150 C470,250 520,380 660,450 L640,450 C505,380 460,250 490,150 C510,80 550,30 597,0 Z" fill="#1e3f75"/>
  </svg>
  <div class="cover-brand"><span class="mark"></span><span class="name">CORVANE USA</span></div>
  <p class="welcome">WELCOME TO</p>
  <h1 class="cover-name">CORVANE USA</h1>
  <p class="cover-lede">Lorem ipsum dolor sit amet, consectetur adipiscing elit, sed do tempor incididunt ut labore et dolore magna aliqua.</p>
</section>

<!-- Market advantages -->
<section class="slide s-adv">
  <h2 class="title">CORVANE MARKET <em>ADVANTAGES</em></h2>
  <div class="brand"><span class="mark"></span><span class="name">CORVANE USA</span></div>
  <div class="adv-card" style="left:46px;top:100px"><span class="num">01</span><h3>Factory-Direct Distributor</h3><p>Improved pricing flexibility.</p></div>
  <div class="adv-card" style="left:46px;top:174px"><span class="num">02</span><h3>Unusually Broad FRP Product Line</h3><p>“One-stop Shop”</p></div>
  <div class="adv-card" style="left:46px;top:248px"><span class="num">03</span><h3>Stable and Transparent Pricing</h3><p>Allows for online ordering with no need for “Request a Quote”</p></div>
  <div class="adv-card" style="left:46px;top:322px"><span class="num">04</span><h3>Dual Channel Sales</h3><p>Wholesale (by cargo container) &amp; Retail (small lots)</p></div>
  <div class="adv-card" style="left:418px;top:100px"><span class="num">05</span><h3>U.S. Market Presence</h3><p>Clients often reference superior customer service</p></div>
  <div class="adv-card" style="left:418px;top:174px;padding-top:9px"><span class="num">06</span><h3>Cost Advantage from Turkish Supply Chain Advantages</h3><p style="margin-top:3px">Competitive costs with China and India competitors</p></div>
  <div class="adv-card" style="left:418px;top:248px"><span class="num">07</span><h3>Favorable U.S. Tariff Position</h3><p>Superior position to China competitors</p></div>
  <div class="adv-card" style="left:418px;top:322px"><span class="num">08</span><h3>Lower Fixed Costs</h3><p>Automate &amp; leverage AI to reduce the need for staff.</p></div>
  <div class="footer"></div><p class="copyright">© Copyrights 2025 | All Rights Reserved</p><span class="pagenum">05</span>
</section>

<!-- Table of content -->
<section class="slide s-toc">
  <h2 class="title" style="top:60px">TABLE OF <em>CONTENT</em></h2>
  <div class="brand" style="top:62px"><span class="mark"></span><span class="name">CORVANE USA</span></div>
  <div class="toc-num" style="left:46px;top:122px">01</div>
  <div class="toc-body" style="left:121px;top:122px"><h3>Lorem ipsum dolor sit amet</h3><p>Lorem ipsum dolor sit amet, consectetur adipiscing elit, sed do tempor incididunt ut labore</p></div>
  <div class="toc-num" style="left:46px;top:205px">02</div>
  <div class="toc-body" style="left:121px;top:205px"><h3>Lorem ipsum dolor sit amet</h3><p>Lorem ipsum dolor sit amet, consectetur adipiscing elit, sed do tempor incididunt ut labore</p></div>
  <div class="toc-num" style="left:46px;top:288px">03</div>
  <div class="toc-body" style="left:121px;top:288px"><h3>Lorem ipsum dolor sit amet</h3><p>Lorem ipsum dolor sit amet, consectetur adipiscing elit, sed do tempor incididunt ut labore</p></div>
  <div class="toc-num" style="left:414px;top:122px">04</div>
  <div class="toc-body" style="left:489px;top:122px"><h3>Lorem ipsum dolor sit amet</h3><p>Lorem ipsum dolor sit amet, consectetur adipiscing elit, sed do tempor incididunt ut labore</p></div>
  <div class="toc-num" style="left:414px;top:205px">05</div>
  <div class="toc-body" style="left:489px;top:205px"><h3>Lorem ipsum dolor sit amet</h3><p>Lorem ipsum dolor sit amet, consectetur adipiscing elit, sed do tempor incididunt ut labore</p></div>
  <div class="toc-num" style="left:414px;top:288px">06</div>
  <div class="toc-body" style="left:489px;top:288px"><h3>Lorem ipsum dolor sit amet</h3><p>Lorem ipsum dolor sit amet, consectetur adipiscing elit, sed do tempor incididunt ut labore</p></div>
  <div class="footer"></div><p class="copyright">© Copyrights 2025 | All Rights Reserved</p><span class="pagenum">02</span>
</section>

<!-- Business plan overview -->
<section class="slide s-plan">
  <h2 class="title" style="top:26px">BUSINESS PLAN <em>OVERVIEW</em></h2>
  <div class="brand" style="top:62px"><span class="mark"></span><span class="name">CORVANE USA</span></div>
  <div class="plan-img" role="img" aria-label="Palm-lined avenue in South Florida" style="left:46px;background:linear-gradient(180deg,#3f7fc4 0%,#5e8a4a 55%,#7a8f6a 100%)"></div>
  <div class="plan-img" role="img" aria-label="Two colleagues discussing work on a tablet" style="left:227px;background:linear-gradient(135deg,#e4e6ea 0%,#b9a391 60%,#8b8f97 100%)"></div>
  <div class="plan-img" role="img" aria-label="Textile production line inside a modern plant" style="left:409px;background:linear-gradient(180deg,#2c4d83 0%,#4c7fb6 55%,#c28a3a 100%)"></div>
  <div class="plan-img" role="img" aria-label="Warehouse with forklift and stacked boxes" style="left:590px;background:linear-gradient(135deg,#b68c5e 0%,#8a6a4a 55%,#c99b3e 100%)"></div>
  <div class="plan-col" style="left:46px"><h3>Address South Florida Market to Prove Operations</h3><p>Focus on construction industry.</p></div>
  <div class="plan-col" style="left:227px"><h3>Strong Web Presence</h3><p style="margin-top:14px">Search ads, web storefront, marketplace storefront, etc.</p></div>
  <div class="plan-col" style="left:409px"><h3>Strong Technological Base</h3><p>Online store provide real time pricing (almost all large competitors require request a quote), integrated inventory control and accounting.</p></div>
  <div class="plan-col" style="left:590px"><h3>Inventory &amp; Warehouse</h3><p style="margin-top:14px">Begin with inventory focused on key products and scale to match market demand. Lease warehouse to support scaled inventory.</p></div>
  <div class="footer"></div><p class="copyright">© Copyrights 2025 | All Rights Reserved</p><span class="pagenum">06</span>
</section>

<!-- Situational overview -->
<section class="slide s-situ">
  <div class="situ-photo" role="img" aria-label="Blue-toned spinning mill interior with rows of yarn bobbins"></div>
  <div class="brand" style="top:62px"><span class="mark"></span><span class="name">CORVANE USA</span></div>
  <h2 class="title situ-title">SITUATIONAL <em>OVERVIEW</em></h2>
  <div class="situ-col" style="left:278px;width:250px">
    <div class="item">Corvane USA is the exclusive distributor in North America for Corvane Fiber Reinforced Resins Composite Technologies of Turkey.</div>
    <div class="item">Product portfolio includes:
      <ul><li>Fiber Reinforced Plastic (FRP) Grating.</li><li>FRP Laminated Sheet.</li><li>FRP Pultruded Shapes.</li><li>FRP Compression Molded Shapes.</li></ul>
    </div>
    <div class="item">All products are manufactured at the Corvane factory near the Port of Izmir, Turkey.</div>
    <div class="item">Corvane Turkey is wholly owned by Mr. Deniz Arkan.</div>
    <div class="item">Corvane USA is jointly owned by Deniz Arkan and Marco Lentini.</div>
  </div>
  <div class="situ-col" style="left:557px;width:205px">
    <div class="item" style="margin-bottom:0">The U.S. business plan is being executed in two phases:</div>
    <p class="phase">Phase 2 – Growth</p>
    <ul class="phase-list"><li>Proven product-market fit with 4 large recurring customers.</li><li>Gained deep understanding of the U.S. and Americas market.</li><li>Identified and addressed testing &amp; certification requirements.</li><li>Specified custom tooling to meet U.S. standards.</li><li>Developed a full set of sales &amp; technical materials in imperial units.</li><li>Identified clear competitive differentiators.</li></ul>
    <p class="phase">Phase 2 – Growth</p>
    <ul class="phase-list"><li>Now preparing to fund and scale the business.</li></ul>
  </div>
  <div class="footer"></div><p class="copyright" style="color:#fff">© Copyrights 2025 | All Rights Reserved</p><span class="pagenum">03</span>
</section>

<!-- Blank title slide -->
<section class="slide s-blank">
  <h2 class="title" style="top:26px">TITLE <em>HERE</em></h2>
  <div class="brand" style="top:62px"><span class="mark"></span><span class="name">CORVANE USA</span></div>
  <div class="watermark"><span class="mark"></span><span class="name">CORVANE USA</span></div>
  <div class="footer"></div><p class="copyright">© Copyrights 2025 | All Rights Reserved</p><span class="pagenum">07</span>
</section>

<!-- US FRP market overview -->
<section class="slide s-market">
  <h2 class="title" style="top:16px">US FRP MARKET <em>OVERVIEW</em></h2>
  <div class="brand" style="top:62px"><span class="mark"></span><span class="name">CORVANE USA</span></div>
  <p class="market-lede">US Market Size (2024): Estimated at $24.03 billion, with projections to reach $43.67 billion by 2032, reflecting a Compound Annual Growth Rate (CAGR) of 7.6%.</p>
  <div class="icon-box" style="left:46px;top:134px">
    <svg width="26" height="26" viewBox="0 0 26 26" fill="none" stroke="var(--red)" stroke-width="1.4"><path d="M3 23h20M6 23v-5M11 23v-8M16 23v-6M21 23v-11M4 14l6-5 5 3 8-8M19 4h4v4"/></svg>
  </div>
  <div class="icon-box" style="left:424px;top:134px">
    <svg width="26" height="26" viewBox="0 0 26 26" fill="none" stroke="var(--red)" stroke-width="1.4"><path d="M13 14V7M13 9c-3 0-5-2-5-5 3 0 5 2 5 5zM13 9c3 0 5-2 5-5-3 0-5 2-5 5zM3 17h5l4 2h5M3 17v6h4l6 1 10-6-2-2-7 3"/></svg>
  </div>
  <div class="mk-col" style="left:108px">
    <h2>KEY GROWTH DRIVERS:</h2>
    <h4>AUTOMOTIVE SECTOR:</h4><p>Increasing demand for lightweight, fuel-efficient vehicles is driving the adoption of FRP composites.</p>
    <h4>AEROSPACE INDUSTRY:</h4><p>FRP materials are favored for their high strength-to-weight ratio, contributing to improved aircraft performance.</p>
    <h4>CONSTRUCTION &amp; INFRASTRUCTURE:</h4><p>FRP's corrosion resistance and durability make it ideal for bridges, pipelines, and building reinforcements.</p>
    <h4>MARINE APPLICATIONS:</h4><p>FRP's resistance to moisture and chemicals enhances its suitability for shipbuilding and offshore structures.</p>
  </div>
  <div class="mk-col" style="left:486px">
    <h2>RECENT DEVELOPMENTS:</h2>
    <h4>INFRASTRUCTURE INVESTMENTS:</h4><p>The U.S. government's focus on infrastructure modernization is boosting the demand for FRP materials in construction projects.</p>
    <h4>SUSTAINABILITY INITIATIVES:</h4><p>There's a growing emphasis on developing recyclable and bio-based FRP composites to meet environmental regulations.</p>
    <h4>TECHNOLOGICAL ADVANCEMENTS:</h4><p>Innovations in manufacturing processes, such as resin transfer molding (RTM) and pultrusion, are enhancing production efficiency and product quality.</p>
  </div>
  <div class="footer"></div><p class="copyright">© Copyrights 2025 | All Rights Reserved</p><span class="pagenum">04</span>
</section>

<!-- Thank you -->
<section class="slide s-thanks">
  <svg class="abs" width="801" height="450" viewBox="0 0 801 450">
    <path d="M150,450 C190,310 320,236 440,236 C560,236 650,300 705,450 Z" fill="var(--red)"/>
    <path d="M178,450 C215,325 330,252 436,252 C550,252 622,315 670,450 Z" fill="#1a3566"/>
    <path d="M196,450 C232,335 335,264 432,264 C540,264 602,330 642,450 Z" fill="#f1f3f7"/>
  </svg>
  <div class="thanks-brand"><span class="mark"></span><span class="name">CORVANE USA</span></div>
  <h2 class="thanks-word">THANK <em>YOU</em></h2>
  <p class="thanks-lede">Lorem ipsum dolor sit amet, consectetur adipiscing elit, sed do tempor incididunt ut labore et dolore magna aliqua.</p>
</section>

</body>
</html>
```